VANDIR/ VANDIR GREY Business Card

We have two brands that we would like to show one 1 business card (front and back). We would to incorporate two different logos on one card (VANDIR and VANDIR GREY). Card can be two sided. Simple, sleek and professional.

We are a senior living provider.

www.vandir-example.com
www.vandirgrey-example.com

Target Market(s)

Professionals

Industry/Entity Type

Business

Font styles to use
Serif

Colors

Designer to choose colors to be used in the design.

Requirements
Must have
• Space for EMAIL, PHONE, WEBSITE
Nice to have
• Raised lettering or gloss lettering

```html
<!DOCTYPE html>
<html lang="en">
<head>
<meta charset="utf-8">
<title>Vandir Grey Business Card</title>
<link rel="stylesheet" href="https://fonts.googleapis.com/css2?family=Cinzel:wght@400;600&family=Crimson+Text:ital,wght@0,400;0,600;1,400&family=Open+Sans:wght@400&display=swap">
<style>
  :root {
    --backdrop: #3a3a3a;
    --card-black: #232323;
    --emboss: #8e8e8e;
    --paper: #f7f7f7;
    --ink: #141414;
    --gold: #c9a24e;
    --slate: #8a8a8a;
    --muted-white: #e8e8e8;
  }
  * { margin: 0; padding: 0; box-sizing: border-box; }
  html, body { width: 799px; height: 1200px; overflow: hidden; }
  body {
    background: var(--backdrop);
    position: relative;
    font-family: "Crimson Text", Georgia, serif;
  }
  .card {
    position: absolute;
    left: 90px;
    width: 620px;
    height: 354px;
    overflow: hidden;
    box-shadow: 0 14px 30px rgba(0,0,0,0.45);
  }
  /* Front */
  .card--front { top: 140px; background: var(--card-black); }
  .front-brand {
    position: absolute;
    left: 0; right: 0; top: 118px;
    display: flex; align-items: center; justify-content: center; gap: 22px;
  }
  .front-brand__square {
    width: 54px; height: 54px;
    background: var(--emboss);
  }
  .front-brand__name {
    font-family: "Cinzel", "Times New Roman", serif;
    font-size: 78px; font-weight: 400;
    letter-spacing: 4px;
    color: var(--emboss);
    line-height: 1;
  }
  .front-url {
    position: absolute;
    left: 0; right: 0; bottom: 58px;
    text-align: center;
    font-size: 15px;
    letter-spacing: 6px;
    color: var(--muted-white);
  }
  /* Back */
  .card--back { top: 706px; background: var(--paper); }
  .back-bands { position: absolute; inset: 0; }
  .back-brand {
    position: absolute; left: 56px; top: 48px;
  }
  .back-brand__name {
    font-family: "Cinzel", "Times New Roman", serif;
    font-size: 44px; font-weight: 600;
    color: var(--ink);
    letter-spacing: 1px;
    line-height: 1;
  }
  .back-brand__tagline {
    font-family: "Open Sans", Arial, sans-serif;
    font-size: 19px;
    color: var(--ink);
    margin-top: 6px;
    margin-left: 2px;
  }
  .holder { position: absolute; left: 56px; top: 184px; }
  .holder__name {
    font-family: "Cinzel", "Times New Roman", serif;
    font-size: 25px; font-weight: 600; line-height: 1;
    color: var(--ink);
  }
  .holder__name .first { color: var(--gold); }
  .holder__role { font-style: italic; font-size: 15px; color: var(--ink); }
  .contacts {
    position: absolute; left: 338px; top: 180px;
    list-style: none;
  }
  .contacts li {
    display: flex; align-items: center; gap: 12px;
    font-size: 17px; color: var(--ink); line-height: 24px;
  }
  .contacts svg { width: 13px; height: 13px; fill: var(--gold); flex: none; }
  .back-url {
    position: absolute; left: 300px; bottom: 22px;
    font-size: 18px; color: var(--ink);
  }
</style>
</head>
<body>
  <section class="card card--front">
    <div class="front-brand">
      <span class="front-brand__square"></span>
      <span class="front-brand__name">VANDIR</span>
    </div>
    <p class="front-url">www.vandir-example.com</p>
  </section>

  <section class="card card--back">
    <svg class="back-bands" viewBox="0 0 620 354" preserveAspectRatio="none" aria-hidden="true">
      <rect x="0" y="262" width="620" height="20" fill="var(--slate)"/>
      <polygon points="0,282 250,282 250,354 0,354" fill="var(--paper)"/>
      <polygon points="230,354 292,290 620,290 620,354" fill="var(--gold)"/>
    </svg>
    <div class="back-brand">
      <div class="back-brand__name">VANDIR GREY</div>
      <div class="back-brand__tagline">Executive Personal Care Services</div>
    </div>
    <div class="holder">
      <div class="holder__name"><span class="first">ELENA</span> MARSH</div>
      <div class="holder__role">Managing Director</div>
    </div>
    <ul class="contacts">
      <li><svg viewBox="0 0 16 16"><path d="M3 1h3l1.5 4-2 1.2a9 9 0 0 0 4.3 4.3L11 8.5l4 1.5v3a2 2 0 0 1-2 2A12 12 0 0 1 1 3a2 2 0 0 1 2-2z"/></svg>208-555-0147</li>
      <li><svg viewBox="0 0 16 16"><path d="M1 3h14v10H1z M1 3l7 6 7-6" stroke="var(--paper)" stroke-width="1"/></svg>talk@vandirgrey-example.com</li>
      <li><svg viewBox="0 0 16 16"><circle cx="8" cy="8" r="7"/><path d="M1 8h14M8 1v14" stroke="var(--paper)" stroke-width="1"/></svg>www.vandirgrey-example.com</li>
    </ul>
    <p class="back-url">www.vandir-example.com</p>
  </section>
</body>
</html>
```